4 Page Music Brochure design

We need assistance in designing a 4 Page A4 (A3 folded) Brochure promoting International Music Tour options for school groups. We have included text in the brief as well as images to be used in the brochure.

```html
<!DOCTYPE html>
<html lang="en">
<head>
<meta charset="utf-8">
<title>Meridian Group Travel – Music Tours Brochure</title>
<link href="https://fonts.googleapis.com/css2?family=Roboto:wght@400;500;700&family=Open+Sans:wght@400;600&display=swap" rel="stylesheet">
<style>
:root{
  --red:#b5132a;
  --red-deep:#8e0a22;
  --grey-bg:#d3d3d3;
  --grey-dark:#444;
  --grey-mid:#6e6e6e;
  --ink:#333;
  --paper:#fff;
}
*{box-sizing:border-box;margin:0;padding:0}
html,body{width:1200px;height:1200px;overflow:hidden}
body{background:var(--grey-bg);position:relative;font-family:"Open Sans",Arial,sans-serif;color:var(--ink)}
.spread{position:absolute;left:246px;width:721px;height:513px;background:var(--paper)}
.spread--outer{top:61px}
.spread--inner{top:625px}
.abs{position:absolute}
.brand{font-family:"Roboto",Arial,sans-serif;font-weight:700;color:var(--red);line-height:.95;letter-spacing:-.3px}
.brand span{display:block}
.brand .b1{font-size:21px}
.brand .b2{font-size:14px}
.photo{position:absolute}
.small{font-size:5.2px;line-height:1.42;text-align:justify}

/* back cover */
.contact-bar{left:0;top:429px;width:10px;height:60px;background:var(--red)}
.contact{left:25px;top:428px;font-family:"Roboto",Arial,sans-serif}
.contact h3{font-size:15px;font-weight:500;color:#222;margin-bottom:2px}
.contact .phone{font-size:15px;font-weight:500;display:flex;align-items:center;gap:4px;margin-bottom:3px}
.contact .line{font-size:7.5px;display:flex;align-items:center;gap:6px;margin-bottom:4px;font-family:"Open Sans",Arial,sans-serif}
.back-brand{left:174px;top:447px}

/* front cover */
.cover-brand{left:484px;top:12px;text-align:left;background:#fff;padding:6px 10px}
.cover-photo{left:360px;top:43px;width:361px;height:202px;background:linear-gradient(180deg,#fff 0%,#f7cf5a 18%,#e99a2e 45%,#6f7d8f 72%,#3d4b5e 100%)}
.headline{left:360px;top:245px;width:361px;height:50px;background:linear-gradient(90deg,var(--red),var(--red-deep));color:#fff;font-family:"Roboto",Arial,sans-serif;font-size:16px;line-height:1.2;padding:6px 16px}
.intro{left:376px;top:305px;width:202px}
.intro p{margin-bottom:6px}
.assist-title{left:376px;top:390px;font-family:"Roboto",Arial,sans-serif;font-weight:500;font-size:10px;color:var(--red)}
.assist{left:376px;top:409px;width:210px;display:grid;grid-template-columns:1fr 1fr;column-gap:8px;font-family:"Roboto",Arial,sans-serif;font-size:6.5px;color:#222}
.assist ul{list-style:none}
.assist li{display:flex;gap:4px;margin-bottom:5px;line-height:1.3}
.assist li svg{flex:none;margin-top:1px}
.founded{left:587px;top:306px;width:134px;height:183px;background:linear-gradient(180deg,var(--red),var(--red-deep))}
.founded .photo{left:13px;top:13px;width:109px;height:102px;border:2px solid #fff;border-radius:0 0 16px 0;background:linear-gradient(135deg,#7a4a1e,#c9913f 45%,#3b2410)}
.founded p{position:absolute;left:14px;top:128px;width:94px;color:#fff;font-family:"Roboto",Arial,sans-serif;font-weight:500;font-size:7.6px;line-height:1.32;text-align:justify}

/* inner spread */
.inner-brand{left:25px;top:24px}
.rule{left:152px;top:38px;width:208px;height:3px;background:#8a8a8a}
.merge{left:25px;top:68px;width:320px;font-family:"Roboto",Arial,sans-serif;font-size:12.3px;line-height:1.24}
.merge .lead{color:#222}
.merge .tail{color:var(--red)}
.since{left:25px;top:127px;width:320px}
.card{position:absolute;width:332px;height:122px;display:flex;color:#fff}
.card .photo{position:relative;width:149px;height:100%;border:2px solid #9a9a9a}
.card .text{flex:1;padding:12px 12px 0 12px}
.card h4{font-family:"Roboto",Arial,sans-serif;font-weight:500;font-size:9.6px;line-height:1.3;margin-bottom:9px}
.card .small{font-size:5px;margin-bottom:6px}
.card--red .text{background:linear-gradient(90deg,var(--red),var(--red-deep))}
.card--grey .text{background:linear-gradient(90deg,#5a5a5a,#8a8a8a)}
.photo--left{border-radius:14px 0 24px 0}
.photo--right{border-radius:0 14px 0 24px;order:2}
.japan{left:376px;top:23px}
.japan .photo{background:linear-gradient(90deg,#3b1208,#d0401c 40%,#8d2310 70%,#2a0f08)}
.choir{left:12px;top:173px}
.choir .photo{background:linear-gradient(180deg,#b9c8d8,#8d8f8c 55%,#4d4a42)}
.euro{left:376px;top:173px}
.euro .photo{background:linear-gradient(135deg,#6b3a15,#c78a3a 45%,#3a2211)}
.hall{left:12px;top:324px}
.hall .photo{background:linear-gradient(180deg,#1f160f,#7d4a1c 55%,#2b2118)}
.usa{left:376px;top:324px}
.usa .photo{background:linear-gradient(180deg,#7b7a78,#b52b2b 55%,#5a1a1a)}
.footer{left:0;top:475px;width:721px;height:38px;background:var(--grey-dark);color:#fff;font-family:"Roboto",Arial,sans-serif;font-size:12px;display:flex;align-items:center}
.footer span{width:50%;text-align:center}
</style>
</head>
<body>

<section class="spread spread--outer">
  <div class="abs contact-bar"></div>
  <div class="abs contact">
    <h3>Contact us</h3>
    <div class="phone"><svg width="10" height="10" viewBox="0 0 10 10"><circle cx="5" cy="5" r="5" fill="#222"/><path d="M3.2 2.4l1 1-.5.7c.4.8 1 1.4 1.8 1.8l.7-.5 1 1-.6.8C4.8 7 3 5.2 2.8 3z" fill="#fff"/></svg>(02) 5550 1234</div>
    <div class="line"><svg width="9" height="9" viewBox="0 0 10 10"><circle cx="5" cy="5" r="5" fill="#222"/><rect x="2.5" y="3.3" width="5" height="3.4" fill="#fff"/></svg>hello@meridiangroup.travel</div>
    <div class="line"><svg width="9" height="9" viewBox="0 0 10 10" fill="none" stroke="#222" stroke-width=".9"><circle cx="5" cy="5" r="4.3"/><ellipse cx="5" cy="5" rx="1.8" ry="4.3"/><path d="M.7 5h8.6"/></svg>www.meridiangroup.travel</div>
  </div>
  <div class="abs brand back-brand"><span class="b1">MERIDIAN</span><span class="b2">GROUP TRAVEL</span></div>

  <div class="photo cover-photo" role="img" aria-label="Passenger jet on an airport apron at sunset"></div>
  <div class="abs brand cover-brand"><span class="b1">MERIDIAN</span><span class="b2">GROUP TRAVEL</span></div>
  <h1 class="abs headline">PLAY IN VENUES FOR<br>AUDIENCES AROUND THE WORLD</h1>
  <div class="abs intro small">
    <p>Our focus is providing unique opportunities to School &amp; Sports groups that expand the horizons of students, foster personal growth, develop independence and provide memories that last a lifetime.</p>
    <p>Our understanding of the unique requirements of group travel and our personalised approach makes us the ideal choice in planning, sourcing and managing the perfect tour for your school or club. Our ever-growing global network allows us to offer exclusive experiences that are inaccessible to others. Our dedicated Tour Coordinators thoroughly consult with staff to tailor an itinerary and tour management plan that meets each unique set of requirements.</p>
  </div>
  <h2 class="abs assist-title">We can assist in providing:</h2>
  <div class="abs assist">
    <ul>
      <li><svg width="6" height="6" viewBox="0 0 6 6"><circle cx="3" cy="3" r="2.6" fill="none" stroke="#b5132a" stroke-width=".6"/><path d="M1.8 3l.8.8 1.6-1.6" fill="none" stroke="#b5132a" stroke-width=".6"/></svg>Customised Itineraries</li>
      <li><svg width="6" height="6" viewBox="0 0 6 6"><circle cx="3" cy="3" r="2.6" fill="none" stroke="#b5132a" stroke-width=".6"/><path d="M1.8 3l.8.8 1.6-1.6" fill="none" stroke="#b5132a" stroke-width=".6"/></svg>Negotiated Group Discounts on airfares, accommodation, transport and activities</li>
      <li><svg width="6" height="6" viewBox="0 0 6 6"><circle cx="3" cy="3" r="2.6" fill="none" stroke="#b5132a" stroke-width=".6"/><path d="M1.8 3l.8.8 1.6-1.6" fill="none" stroke="#b5132a" stroke-width=".6"/></svg>Festival/event entry</li>
      <li><svg width="6" height="6" viewBox="0 0 6 6"><circle cx="3" cy="3" r="2.6" fill="none" stroke="#b5132a" stroke-width=".6"/><path d="M1.8 3l.8.8 1.6-1.6" fill="none" stroke="#b5132a" stroke-width=".6"/></svg>Workshops with clinicians</li>
      <li><svg width="6" height="6" viewBox="0 0 6 6"><circle cx="3" cy="3" r="2.6" fill="none" stroke="#b5132a" stroke-width=".6"/><path d="M1.8 3l.8.8 1.6-1.6" fill="none" stroke="#b5132a" stroke-width=".6"/></svg>School exchanges</li>
    </ul>
    <ul>
      <li><svg width="6" height="6" viewBox="0 0 6 6"><circle cx="3" cy="3" r="2.6" fill="none" stroke="#b5132a" stroke-width=".6"/><path d="M1.8 3l.8.8 1.6-1.6" fill="none" stroke="#b5132a" stroke-width=".6"/></svg>Public performances</li>
      <li><svg width="6" height="6" viewBox="0 0 6 6"><circle cx="3" cy="3" r="2.6" fill="none" stroke="#b5132a" stroke-width=".6"/><path d="M1.8 3l.8.8 1.6-1.6" fill="none" stroke="#b5132a" stroke-width=".6"/></svg>Instrument rental</li>
      <li><svg width="6" height="6" viewBox="0 0 6 6"><circle cx="3" cy="3" r="2.6" fill="none" stroke="#b5132a" stroke-width=".6"/><path d="M1.8 3l.8.8 1.6-1.6" fill="none" stroke="#b5132a" stroke-width=".6"/></svg>Venue hire</li>
      <li><svg width="6" height="6" viewBox="0 0 6 6"><circle cx="3" cy="3" r="2.6" fill="none" stroke="#b5132a" stroke-width=".6"/><path d="M1.8 3l.8.8 1.6-1.6" fill="none" stroke="#b5132a" stroke-width=".6"/></svg>Trusted, Quality Suppliers</li>
      <li><svg width="6" height="6" viewBox="0 0 6 6"><circle cx="3" cy="3" r="2.6" fill="none" stroke="#b5132a" stroke-width=".6"/><path d="M1.8 3l.8.8 1.6-1.6" fill="none" stroke="#b5132a" stroke-width=".6"/></svg>Sightseeing</li>
      <li><svg width="6" height="6" viewBox="0 0 6 6"><circle cx="3" cy="3" r="2.6" fill="none" stroke="#b5132a" stroke-width=".6"/><path d="M1.8 3l.8.8 1.6-1.6" fill="none" stroke="#b5132a" stroke-width=".6"/></svg>Expert Guides and Tour Escorts</li>
    </ul>
  </div>
  <div class="abs founded">
    <div class="photo" role="img" aria-label="Ornate opera house auditorium with tiered gold balconies"></div>
    <p>Meridian Group Travel was established in 2001, to provide once in a lifetime experiences.</p>
  </div>
</section>

<section class="spread spread--inner">
  <div class="abs brand inner-brand"><span class="b1">MERIDIAN</span><span class="b2">GROUP TRAVEL</span></div>
  <div class="abs rule"></div>
  <h2 class="abs merge"><span class="lead">Meridian Sporting Events and Meridian Education Tours </span><span class="tail">are now together under the one banner Meridian Group Travel</span></h2>
  <p class="abs since small">Since our first international basketball tour in 2001, we have now grown to offer more sports including Rugby, Football, Netball, Hockey, Cricket, Cheerleading, Ultimate Frisbee, Gridiron, Lacrosse, Softball and Swimming to destinations all over the globe.</p>

  <article class="card card--red japan">
    <div class="photo photo--left" role="img" aria-label="Path through a tunnel of red torii gates"></div>
    <div class="text">
      <h4>Japan Music Tours</h4>
      <p class="small">Travel to the land of the Rising Sun and take part in school exchanges, public performances and the chance to perform at iconic theme parks Tokyo Fantasy Park and Cinema Studios Park Japan.</p>
      <p class="small">Students will have the opportunity take a Japanese Cooking Class, partake in a Traditional Japanese Tea Ceremony, see a Kabuki show, and ride the bullet train.</p>
    </div>
  </article>

  <article class="card card--red choir">
    <div class="photo photo--left" role="img" aria-label="Gothic cathedral towers above a historic town square"></div>
    <div class="text">
      <h4>Global Choir Festival (5th to the 15th of July 2020)</h4>
      <p class="small">Join the biggest Choral Music event in the world with Choirs from over 80 different countries and regions, taking part in adjudicated performances, individual coaching, and singing workshops. Held in Belgium in the cities Antwerp and Ghent, this is a fantastic opportunity perform on the world stage as well as take in the rich history of the Flanders region. With the option to extend your trip to include France, Germany, Italy, Austria or other nearby European Countries.</p>
    </div>
  </article>

  <article class="card card--grey euro">
    <div class="photo photo--right" role="img" aria-label="Grand concert hall interior with gilded balconies"></div>
    <div class="text">
      <h4 style="margin-top:6px">European Instrumental Tours</h4>
      <p class="small">Play in Austria, France, Germany, the United Kingdom, or wherever your heart desires, you band, orchestra or ensemble will have the opportunity to perform at concert halls across Europe.</p>
      <p class="small">As well as opportunities to participate in festivals, public performances and workshop with music professionals.</p>
    </div>
  </article>

  <article class="card card--grey hall">
    <div class="photo photo--right" role="img" aria-label="Historic concert hall facade lit up at night"></div>
    <div class="text">
      <h4>Lexington Concert Hall</h4>
      <p class="small">The once in a life time opportunity to perform on one of the world's most famous music venues.</p>
      <p class="small">Choirs will also have the opportunity to participate in performances, clinics, workshops, and exchanges.</p>
      <p class="small">Based in New York City, there will also be the chance to include stops in Washington DC, Los Angeles, or San Francisco on to your trip.</p>
    </div>
  </article>

  <article class="card card--red usa">
    <div class="photo photo--left" role="img" aria-label="Marching band in red uniforms parading down a city street"></div>
    <div class="text">
      <h4>US Music Road Trip</h4>
      <p class="small">Trace a path across the US journeying from Jazz to Blues to Soul onto Rock'n'Roll before finishing in Country Music capital of the world – Nashville.</p>
      <p class="small">You will visit New Orleans, Memphis and Nashville where you will have the opportunity to perform at unique venues, undertake school exchanges and participate in workshops with musicians and professionals.</p>
    </div>
  </article>

  <footer class="abs footer"><span>www.meridiangroup.travel</span><span>www.meridiangroup.travel</span></footer>
</section>

</body>
</html>
```